Dashboard Elements

Hello – looking for someone to create dashboard elements.
I’ve already basically designed all these elements – but I need someone to take what I’ve designed and make it look like an actual dashboard UI, like an app - assuming using some kind of dashboard UI kit (but however you would like to get it done is fine). It can look just like mine or try something different, as long as it matches the color scheme webpage that I’m going to out it on – see the page here. I’m ok with making it dark, maybe that would look better – again as long as it matches the webpage (https://www.plandeck.io/file/7KqWmb2TxRpLnVc4Hd8Fs3/Webpage-with-placeholders?node-id=0%3A1). Please note, you do not need to put anything on the webpage or do anything with this Figma file, this is just a reference so you can color/stylize it accordingly.

The attached Powerpoint file has everything you need - make sure to zoom all the way out to see everything on the slides.

Here are the Dashboard elements needed (this will all make sense when you look at the PPT):
Dashboard 1
Dashboard 1 – expanded view A
Dashboard 1 – expanded view B
View Source button by itself
Source Document Viewer 1 and 2 (these are exactly the same just with a different image inside)*
Dashboard 2 (only slightly different than Dashboard 1, just extended with extra headings
Table of Contents
Searchbar and Source Doc by itself
*the documents in the source document viewers should still look like documents - they don’t need to look like part of the UI, because this is a document viewer – you can restyle/recolor if necessary or just leave these as is.
- Colors must match color scheme of webpage, attached and on Figma link (images there currently are only placeholders) – ok to go dark as long as it matches
- Must look sleek, clean, realistic
- Don’t add any pictures of people or change the text.
- In case it’s not clear, this is what I mean by the concept of Dashboard UI - https://www.quillbin.com/shard/s7/sh/8c1d2fa0-42b7-9a3e-7d5c-03b8e1f9a6d4/71c4e2a09b3f6d58e2a1c7f04b9d3e62
- Must be sent in an editable file, I may need to be edit text and other elements
- If you are going to send a sample, please make sure it’s part of the dashboard itself, not just the table of contents etc

Ideally hoping to find someone I can continue working with as I'll have a lot more graphic design work needed coming up.

Thank you!

```html
<!DOCTYPE html>
<html lang="en">
<head>
<meta charset="utf-8">
<title>Dashboard 1 – HCC Summary</title>
<link rel="stylesheet" href="https://fonts.googleapis.com/css2?family=Open+Sans:wght@400;500;600;700&display=swap">
<style>
  :root {
    --bg-deep: #0e0b22;
    --panel: #1c1a38;
    --panel-violet: #2e2a55;
    --panel-teal: #173a44;
    --frame: #8a8a9a;
    --side-top: #0d56a8;
    --side-bottom: #17a89a;
    --active-band: #1cbcb8;
    --teal: #2ac4bb;
    --violet: #7b68ee;
    --violet-text: #8d7cf0;
    --white: #ffffff;
    --line: #4a4868;
    --head-line: #b8b8c8;
    --ui-font: "Open Sans", sans-serif;
  }
  * { margin: 0; padding: 0; box-sizing: border-box; }
  html, body { width: 1200px; height: 842px; overflow: hidden; }
  body {
    font-family: var(--ui-font);
    color: var(--white);
    white-space: nowrap;
    background:
      radial-gradient(ellipse 520px 420px at 0% 45%, rgba(91,74,158,.75), transparent 70%),
      radial-gradient(ellipse 600px 420px at 100% 100%, rgba(15,90,90,.8), transparent 70%),
      var(--bg-deep);
    position: relative;
  }
  .dashboard {
    position: absolute; left: 62px; top: 62px; width: 1077px; height: 604px;
    border: 2px solid var(--frame); border-radius: 50px; overflow: hidden;
    background: var(--panel);
  }
  .sidebar {
    position: absolute; left: 0; top: 0; width: 230px; height: 100%;
    background: linear-gradient(170deg, var(--side-top) 0%, #1383a6 45%, var(--side-bottom) 100%);
  }
  .main {
    position: absolute; left: 220px; top: 0; right: 0; bottom: 0;
    border-radius: 40px 0 0 40px; overflow: hidden;
    background: var(--panel);
  }
  .main::before {
    content: ""; position: absolute; left: -60px; top: -220px; width: 640px; height: 520px;
    border-radius: 50%; background: var(--panel-violet); opacity: .75;
  }
  .main::after {
    content: ""; position: absolute; left: 340px; top: 330px; width: 780px; height: 560px;
    border-radius: 50%; background: linear-gradient(160deg, #1c2a42, var(--panel-teal)); opacity: .9;
  }
  .nav-item {
    position: absolute; left: 0; width: 220px; height: 30px;
    display: flex; align-items: center; font-size: 17.5px; font-weight: 500;
  }
  .nav-item .icon { position: absolute; left: 20px; width: 24px; height: 24px; }
  .nav-item .label { position: absolute; left: 56px; }
  .nav-item .toggle { position: absolute; left: 177px; width: 17px; height: 17px; }
  .nav-sub {
    position: absolute; left: 0; top: 121px; width: 220px; height: 26px;
    background: var(--active-band); font-size: 11.5px; padding-left: 56px; line-height: 26px;
  }
  .content { position: absolute; inset: 0; z-index: 1; }
  .abs { position: absolute; }
  .brand { left: 249px; top: 40px; display: flex; align-items: center; gap: 11px; font-size: 24px; letter-spacing: 1.5px; font-weight: 500; line-height: 30px; }
  .brand-square { width: 22px; height: 22px; background: var(--violet); border-radius: 3px; }
  .title-pill {
    left: 520px; top: 38px; width: 258px; height: 35px; border-radius: 5px;
    background: var(--violet); font-size: 23px; font-weight: 600; text-align: center; line-height: 35px;
  }
  .patient-name { left: 825px; top: 36px; font-size: 19px; line-height: 26px; display: flex; align-items: center; gap: 14px; }
  .patient-meta { left: 825px; top: 68px; font-size: 11.5px; line-height: 16px; }
  .bell { left: 1000px; top: 36px; width: 30px; height: 30px; }
  .section-title { left: 254px; top: 119px; display: flex; align-items: center; gap: 14px; font-size: 19px; line-height: 26px; }
  .search {
    left: 442px; top: 120px; width: 228px; height: 30px; border: 1.5px solid var(--teal);
    border-radius: 15px; display: flex; align-items: center; gap: 6px; padding-left: 8px; font-size: 12px;
  }
  .stats { left: 710px; top: 121px; display: flex; align-items: center; font-size: 14px; line-height: 28px; }
  .stat-teal { color: var(--teal); }
  .count-badge {
    display: inline-block; width: 27px; height: 27px; border: 2px solid var(--violet); border-radius: 50%;
    text-align: center; line-height: 23px; font-size: 17px; margin: 0 15px 0 8px;
  }
  .hcc-table { left: 248px; top: 185px; width: 784px; }
  .table-head {
    display: grid; grid-template-columns: 158px 302px 170px 154px; height: 48px;
    border: 1.5px solid var(--head-line); border-radius: 6px; font-size: 14.5px;
  }
  .table-head div { display: flex; align-items: center; justify-content: center; gap: 10px; border-left: 1.5px solid var(--head-line); }
  .table-head div:first-child { border-left: none; }
  .sort { width: 15px; height: 15px; }
  .table-row {
    position: relative; height: 58px; width: 816px; margin-left: -10px;
    border-bottom: 1px solid var(--line);
  }
  .table-row:last-child { border-bottom: none; }
  .table-head + .table-row { margin-top: 10px; }
  .cell { position: absolute; top: 50%; transform: translateY(-50%); }
  .code { left: 46px; font-size: 19px; color: var(--teal); }
  .condition { left: 188px; font-size: 11.6px; }
  .category { left: 541px; font-size: 12.5px; color: var(--violet-text); }
  .raf { left: 687px; font-size: 19px; color: var(--teal); }
  .expand { left: 757px; width: 16px; height: 16px; }
  .caption { position: absolute; top: 714px; font-size: 29px; line-height: 40px; }
  .caption-title { left: 202px; font-weight: 600; }
  .caption-note { left: 441px; top: 710px; }
</style>
</head>
<body>
<svg width="0" height="0" style="position:absolute">
  <defs>
    <symbol id="ring-chevron" viewBox="0 0 20 20"><circle cx="10" cy="10" r="8.5" fill="none" stroke="#fff" stroke-width="1.5"/><path d="M6.5 8.5 10 12l3.5-3.5" fill="none" stroke="#fff" stroke-width="1.6"/></symbol>
    <symbol id="solid-chevron" viewBox="0 0 20 20"><circle cx="10" cy="10" r="10" fill="#8d7cf0"/><path d="M6.3 8.3 10 12l3.7-3.7" fill="none" stroke="#fff" stroke-width="2"/></symbol>
    <symbol id="down" viewBox="0 0 16 16"><path d="M2 5l6 6 6-6" fill="none" stroke="currentColor" stroke-width="2.6"/></symbol>
  </defs>
</svg>

<div class="dashboard">
  <nav class="sidebar">
    <div class="nav-item" style="top:126px">
      <svg class="icon" viewBox="0 0 24 24" fill="none" stroke="#fff" stroke-width="1.5"><path d="M3 17a9 9 0 0 1 18 0"/><path d="M12 17l4-6"/><path d="M6 17h2M16 17h2"/></svg>
      <span class="label">Dashboard</span>
      <svg class="toggle" viewBox="0 0 20 20"><circle cx="10" cy="10" r="10" fill="#fff"/><path d="M6.3 8.3 10 12l3.7-3.7" fill="none" stroke="#1383a6" stroke-width="2"/></svg>
    </div>
    <div class="nav-sub" style="top:167px">HCC Summary</div>
    <div class="nav-item" style="top:206px">
      <svg class="icon" viewBox="0 0 24 24" fill="none" stroke="#fff" stroke-width="1.5"><circle cx="12" cy="8" r="4"/><path d="M4 21v-2a5 5 0 0 1 5-5h6a5 5 0 0 1 5 5v2z"/></svg>
      <span class="label">Admin</span><svg class="toggle"><use href="#ring-chevron"/></svg>
    </div>
    <div class="nav-item" style="top:286px">
      <svg class="icon" viewBox="0 0 24 24" fill="none" stroke="#fff" stroke-width="1.5"><circle cx="12" cy="12" r="3.5"/><circle cx="12" cy="12" r="8" stroke-dasharray="3 2"/></svg>
      <span class="label">Configure</span><svg class="toggle"><use href="#ring-chevron"/></svg>
    </div>
    <div class="nav-item" style="top:366px">
      <svg class="icon" viewBox="0 0 24 24" fill="none" stroke="#fff" stroke-width="1.5"><path d="M3 21h18M6 20v-5M10 20v-8M14 20v-11M18 20v-15"/></svg>
      <span class="label">Diagnostics</span><svg class="toggle"><use href="#ring-chevron"/></svg>
    </div>
    <div class="nav-item" style="top:446px">
      <svg class="icon" viewBox="0 0 24 24" fill="none" stroke="#fff" stroke-width="1.5"><path d="M4 4l16 16M20 4L4 20"/><circle cx="5" cy="5" r="2"/><circle cx="19" cy="19" r="2"/></svg>
      <span class="label">Maintanance</span><svg class="toggle"><use href="#ring-chevron"/></svg>
    </div>
    <div class="nav-item" style="top:527px">
      <svg class="icon" viewBox="0 0 24 24" fill="none" stroke="#fff" stroke-width="1.5"><circle cx="12" cy="12" r="9"/><circle cx="12" cy="12" r="4"/></svg>
      <span class="label">Support</span><svg class="toggle"><use href="#ring-chevron"/></svg>
    </div>
  </nav>

  <main class="main"></main>

  <div class="content">
    <div class="abs brand"><span class="brand-square"></span>VITALWARD</div>
    <div class="abs title-pill">C-CDA Compendium</div>
    <div class="abs patient-name">Patient, Ruth <svg width="18" height="18"><use href="#solid-chevron"/></svg></div>
    <div class="abs patient-meta">Female | 01/11/1951 | Age: 70</div>
    <svg class="abs bell" viewBox="0 0 30 30"><path d="M6 22h18l-2.5-3.5V13a6.5 6.5 0 0 0-13 0v5.5z" fill="#2ac4bb"/><circle cx="15" cy="24.5" r="2.5" fill="#2ac4bb"/><circle cx="23" cy="6" r="5" fill="#fff"/><text x="23" y="8.5" font-size="7" text-anchor="middle" fill="#1c1a38" font-family="Open Sans, sans-serif">3</text></svg>

    <div class="abs section-title">
      <svg width="16" height="16" style="color:#2ac4bb"><use href="#down"/></svg>HCC Summary
    </div>
    <div class="abs search">
      <svg width="20" height="20" viewBox="0 0 20 20" fill="none" stroke="#2ac4bb" stroke-width="1.6"><circle cx="8.5" cy="8.5" r="6.5"/><path d="M13.5 13.5 18 18"/></svg>Search...
    </div>
    <div class="abs stats">
      <span class="stat-teal">RAF: 2.362</span>
      <span style="margin-left:19px">Condition Count</span>
      <span class="count-badge">8</span>
      <span class="stat-teal">ID: 7326472</span>
    </div>

    <div class="abs hcc-table">
      <div class="table-head">
        <div>ICD-10 Code <svg class="sort"><use href="#solid-chevron"/></svg></div>
        <div>Condition <svg class="sort"><use href="#solid-chevron"/></svg></div>
        <div>Catagory <svg class="sort"><use href="#solid-chevron"/></svg></div>
        <div>RAF <svg class="sort"><use href="#solid-chevron"/></svg></div>
      </div>
      <div class="table-row"><span class="cell code">J44.9</span><span class="cell condition">Chronic obstructive pulmonary disease</span><span class="cell category">111</span><span class="cell raf">0.335</span><svg class="cell expand" style="color:#fff"><use href="#down"/></svg></div>
      <div class="table-row"><span class="cell code">F33.1</span><span class="cell condition">Chronic kidney disease, moderate (stage 3)</span><span class="cell category">138</span><span class="cell raf">0.069</span><svg class="cell expand" style="color:#fff"><use href="#down"/></svg></div>
      <div class="table-row"><span class="cell code">F33.0</span><span class="cell condition">Major depressive disorder, recurrent, mild</span><span class="cell category">59</span><span class="cell raf">0.309</span><svg class="cell expand" style="color:#fff"><use href="#down"/></svg></div>
      <div class="table-row"><span class="cell code">I42.9</span><span class="cell condition">cardiomyopathy</span><span class="cell category">85</span><span class="cell raf">0.447</span><svg class="cell expand" style="color:#fff"><use href="#down"/></svg></div>
      <div class="table-row"><span class="cell code">E11.36</span><span class="cell condition">Type 2 diabetes mellitus with diabetic cataract</span><span class="cell category">18</span><span class="cell raf">0.302</span><svg class="cell expand" style="color:#fff"><use href="#down"/></svg></div>
    </div>
  </div>
</div>

<div class="caption caption-title">Dashboard 1</div>
<div class="caption caption-note">*please note other designs are in progress</div>
</body>
</html>
```